Solar energy proposal for homeowners

I am providing households with solar energy proposals, and I need a high-quality brochure that is packaged cleverly to attract the homeowner's attention. Take a look at the one page solar brochure that I have included to get an idea of text and content.

Target Market(s)

Residential Homeowners

Industry/Entity Type

Solar

Requirements
Must have
• High quality document

```html
<!DOCTYPE html>
<html lang="en">
<head>
<meta charset="utf-8">
<title>Solvista Energy – Solar Flyer</title>
<link rel="stylesheet" href="https://fonts.googleapis.com/css2?family=Anton&family=Oswald:wght@600&family=Questrial&family=Lexend:wght@500&display=swap">
<style>
  :root {
    --slate: #58585a;
    --slate-deep: #4f4f51;
    --sky: #12a1d4;
    --lime: #b2d234;
    --sage: #c3d582;
    --ink: #2f3a2a;
    --white: #ffffff;
    --footer-a: #55646f;
    --footer-b: #8aa3b5;
  }
  * { box-sizing: border-box; margin: 0; padding: 0; }
  html, body { width: 1040px; height: 1200px; overflow: hidden; background: #e9e9e9; }
  .flyer { position: relative; width: 1040px; height: 1200px; background: var(--white); overflow: hidden; font-family: "Questrial", sans-serif; }

  .hero-photo {
    position: absolute; left: 0; top: 0; width: 662px; height: 620px;
    background:
      linear-gradient(to bottom, rgba(255,255,255,0) 62%, rgba(255,255,255,0.85) 88%, #fff 100%),
      linear-gradient(160deg, #8d8478 0%, #c7955c 28%, #9a6840 48%, #5a4536 66%, #a98a72 82%, #d9d3cf 100%);
  }
  .intro-panel { position: absolute; left: 662px; top: 0; width: 378px; height: 454px; background: var(--slate); }

  .brand { position: absolute; left: 600px; top: 190px; display: flex; align-items: center; gap: 14px; }
  .brand-mark { width: 34px; height: 34px; background: var(--sky); }
  .brand-name { font-family: "Questrial", sans-serif; font-size: 52px; color: var(--lime); letter-spacing: 1px; white-space: nowrap; }

  .intro-copy { position: absolute; left: 713px; top: 298px; width: 280px; font-size: 13.6px; line-height: 17.6px; color: var(--white); text-align: justify; }

  .banner { position: absolute; left: 0; top: 0; }
  .headline { position: absolute; right: 65px; top: 494px; font-family: "Anton", sans-serif; color: var(--white); text-align: right; font-size: 73px; line-height: 84px; letter-spacing: 0.5px; }
  .headline-rule { position: absolute; left: 784px; top: 676px; width: 107px; height: 11px; background: var(--lime); }

  .features-band { position: absolute; left: 0; top: 730px; width: 1040px; height: 208px; background: var(--sage); }
  .tagline-tab { position: absolute; left: 0; top: 0; }
  .tagline { position: absolute; left: 46px; top: 626px; width: 280px; font-family: "Lexend", sans-serif; font-weight: 500; font-size: 19.5px; line-height: 26px; color: var(--white); }

  .feature { position: absolute; width: 190px; color: var(--ink); }
  .feature-icon { position: absolute; width: 50px; height: 50px; }
  .feature-title { font-family: "Oswald", sans-serif; font-weight: 600; font-size: 15px; line-height: 18.5px; color: var(--ink); }
  .feature-text { font-size: 13px; line-height: 15.5px; margin-top: 4px; }

  .about-band { position: absolute; left: 0; top: 938px; width: 1040px; height: 188px; background: var(--slate); }
  .about-copy { position: absolute; left: 173px; top: 974px; width: 363px; font-size: 12.6px; line-height: 15.4px; color: var(--white); text-align: justify; }

  .install-frame { position: absolute; left: 640px; top: 781px; width: 346px; height: 312px; border: 1.5px solid var(--white); }
  .install-photo {
    position: absolute; left: 654px; top: 774px; width: 343px; height: 308px;
    background: linear-gradient(135deg, #2c4766 0%, #3f5e80 38%, #d8dde2 58%, #f2f3f4 72%, #3b5676 100%);
  }

  .footer { position: absolute; left: 0; top: 1126px; width: 1040px; height: 74px; background: linear-gradient(90deg, var(--footer-a) 0%, var(--footer-b) 50%, var(--footer-a) 100%); color: var(--white); }
  .footer-address { position: absolute; left: 47px; top: 25px; font-size: 12.5px; line-height: 14.5px; }
  .footer-web { position: absolute; left: 0; width: 1040px; top: 26px; text-align: center; font-size: 16px; letter-spacing: 7px; padding-left: 20px; }
  .footer-phone { position: absolute; left: 853px; top: 30px; font-size: 12.5px; }
</style>
</head>
<body>
<main class="flyer">
  <div class="hero-photo" role="img" aria-label="Modern home with rooftop solar panels at sunset"></div>
  <section class="intro-panel"></section>

  <svg class="banner" width="1040" height="1200" viewBox="0 0 1040 1200" aria-hidden="true">
    <path class="banner-outline" d="M290 578 L333 697 Q349 737 398 737 L1040 737" fill="none" stroke="#12a1d4" stroke-width="2"/>
    <path class="banner-shape" d="M380 454 L1040 454 L1040 727 L402 727 Q360 727 342 692 L300 588 Q293 569 301 552 L342 481 Q357 454 380 454 Z" fill="#12a1d4"/>
  </svg>

  <div class="brand">
    <span class="brand-mark"></span>
    <span class="brand-name">Solvista Energy</span>
  </div>

  <p class="intro-copy">Solvista Energy installs and maintains high-efficiency solar systems at our own expense. You pay a flat monthly rental fee. No debt, no liens, just cheaper electricity. Click on our FAQ's to understand how the process works.</p>

  <h1 class="headline">CUT YOUR<br>ELECTRICITY BILL BY</h1>
  <div class="headline-rule"></div>

  <section class="features-band"></section>

  <svg class="tagline-tab" width="1040" height="1200" viewBox="0 0 1040 1200" aria-hidden="true">
    <path d="M0 613 L298 613 Q312 613 318 627 L337 676 L318 725 Q312 739 298 739 L0 739 Z" fill="#b2d234"/>
  </svg>
  <p class="tagline">Because solar should be simple, transparent, and risk-free.</p>

  <svg class="feature-icon" style="left:34px;top:770px" viewBox="0 0 50 50" fill="none" stroke="#2f3a2a" stroke-width="1.4" aria-hidden="true">
    <circle cx="28" cy="12" r="9"/>
    <path d="M28 6 v12 M31 8.5 q-3-2-5.5 0 q-2 2 1 3.5 q4 1.5 2 4 q-2.5 1.8-5.5-.5"/>
    <path d="M3 32 h7 v14 h-7 z M10 34 q8-4 14 0 h7 q3 1 0 3 h-9 M22 37 q12 2 24-7 q3 0 1 3 q-11 10-22 11 h-15"/>
  </svg>
  <div class="feature" style="left:118px;top:771px">
    <h2 class="feature-title">No Money Out of Pocket</h2>
    <p class="feature-text" style="margin-top:14px;font-size:14px">Start saving from day one.</p>
  </div>

  <svg class="feature-icon" style="left:334px;top:765px" viewBox="0 0 50 50" fill="none" stroke="#2f3a2a" stroke-width="1.4" aria-hidden="true">
    <circle cx="25" cy="23" r="11"/>
    <path d="M20 34 v5 h10 v-5 M21 42 h8 M25 14 v14 M25 22 q-4-3-5 0 M25 20 q4-3 5 0 M25 2 v4 M10 8 l3 3 M40 8 l-3 3 M4 23 h4 M42 23 h4"/>
  </svg>
  <div class="feature" style="left:410px;top:771px">
    <h2 class="feature-title">Guaranteed Energy<br>Production</h2>
    <p class="feature-text" style="margin-top:0">You only rely on a system that performs. We credit you for any shortages.</p>
  </div>

  <svg class="feature-icon" style="left:348px;top:852px" viewBox="0 0 50 50" fill="none" stroke="#2f3a2a" stroke-width="1.4" aria-hidden="true">
    <circle cx="25" cy="25" r="22"/>
    <path d="M25 38 v-14 M25 26 q-10 0-11-9 q9-1 11 9 M25 23 q2-9 12-9 q-1 9-12 9"/>
  </svg>
  <div class="feature" style="left:410px;top:859px">
    <h2 class="feature-title">Sustainable Impact</h2>
    <p class="feature-text" style="margin-top:20px">Reduce your carbon footprint effortlessly.</p>
  </div>

  <svg class="feature-icon" style="left:353px;top:855px;width:36px" viewBox="0 0 36 50" fill="none" stroke="#2f3a2a" stroke-width="1.4" aria-hidden="true">
    <path d="M2 2 h24 l8 8 v38 h-32 z M26 2 v8 h8 M8 16 h20 M8 21 h20 M8 26 h20 M8 31 h20 M8 36 h20 M8 41 h14"/>
  </svg>
  <div class="feature" style="left:118px;top:859px">
    <h2 class="feature-title">Simple Rental<br>Agreement</h2>
    <p class="feature-text" style="margin-top:0">Flexible terms for homes and businesses.</p>
  </div>

  <section class="about-band"></section>
  <p class="about-copy">Solvista Energy is redefining how people and businesses access solar. We are not here to sell you power. We are here to help you generate your own. With guaranteed performance, full system maintenance, and flexible rental terms, you can power your property with total peace of mind and none of the long-term financial commitments of traditional solar.</p>

  <div class="install-frame"></div>
  <div class="install-photo" role="img" aria-label="Two technicians in safety vests walking between rows of rooftop solar panels"></div>

  <footer class="footer">
    <p class="footer-address">1420 Meadow Crest Lane<br>Tampa, FL 33602</p>
    <p class="footer-web">solvistaenergy.com</p>
    <p class="footer-phone">555.204.3187</p>
  </footer>
</main>
</body>
</html>
```